INNOVATIVE DESIGN NEEDED FOR FINANCIAL COMPANY

INTERNATIONAL FIRM IN HONG KONG NEEDS A MODERN BUSINESS CARD DESIGN. ONE SIDE ENGLISH OTHER SIDE IN CHINESE. WE ARE OPEN TO CHANGING FONTS AND COLOR. SHOULD BE A CARD THAT IS PROFESSIONAL DEALING WITH HIGH NET WORTH CLIENTELE. BOTH SIDES OF THE CARD WILL BE THE SAME, HOWEVER, THE WORDING ON ONE SIDE WILL BE ENGLISH AND THE OTHER SIDE IN CHINESE (CAN ASSIST IN THE LETTERING - CAN PROVIDE ONCE CARD DESIGN IS ACCEPTED.

Target Market(s)

Hong Kong/CHINA

Contact Information for Business Card

ATTRACTIVE MODERN

```html
<!DOCTYPE html>
<html lang="en">
<head>
<meta charset="utf-8">
<title>Meridian Asset Management – Business Cards</title>
<link href="https://fonts.googleapis.com/css2?family=Lato:wght@400;700&family=Noto+Sans+TC:wght@700&display=swap" rel="stylesheet">
<style>
  :root {
    --backdrop: #9c5c33;
    --kraft-light: #dcbb93;
    --kraft: #c9a27a;
    --kraft-dark: #bb9166;
    --ink: #141008;
  }
  * { margin: 0; padding: 0; box-sizing: border-box; }
  html, body { width: 1200px; height: 900px; overflow: hidden; }
  body {
    background: var(--backdrop);
    font-family: 'Lato', sans-serif;
    color: var(--ink);
    position: relative;
  }
  .business-card {
    position: absolute;
    width: 556px;
    height: 342px;
    background: linear-gradient(150deg, var(--kraft-light) 0%, var(--kraft) 45%, var(--kraft-dark) 100%);
  }
  .business-card--upper { left: 330px; top: 91px; }
  .business-card--lower { left: 331px; top: 470px; }

  .brand {
    position: absolute;
    left: 86px;
    top: 70px;
    display: flex;
    align-items: center;
    gap: 22px;
  }
  .brand__mark {
    width: 56px; height: 56px;
    border-radius: 50%;
    background: var(--ink);
    flex: none;
  }
  .brand__name {
    font-weight: 700;
    color: var(--ink);
    line-height: 1;
  }
  .brand__name-zh {
    display: block;
    font-family: 'Noto Sans TC', 'Lato', sans-serif;
    font-size: 27px;
    letter-spacing: 1px;
  }
  .brand__name-en {
    display: block;
    font-family: 'Lato', sans-serif;
    font-size: 13.5px;
    letter-spacing: 1.6px;
    margin-top: 4px;
  }

  .contact {
    position: absolute;
    left: 0; right: 0;
    top: 170px;
    text-align: center;
    font-size: 15px;
    line-height: 20px;
  }
  .contact__name {
    font-size: 19px;
    font-weight: 700;
    line-height: 22px;
  }
  .contact__role { font-size: 15px; line-height: 20px; }
  .contact__rule {
    width: 196px;
    height: 1px;
    background: var(--ink);
    margin: 6px auto 10px;
  }
  .contact__label { font-weight: 700; }
  .contact__address { margin-top: 0; }
</style>
</head>
<body>

  <section class="business-card business-card--upper">
    <div class="brand">
      <span class="brand__mark"></span>
      <p class="brand__name">
        <span class="brand__name-zh">明澤資產管理有限公司</span>
        <span class="brand__name-en">Meridian Asset Management Ltd</span>
      </p>
    </div>
    <div class="contact">
      <p class="contact__name">DANIEL REED</p>
      <p class="contact__role">Managing Director</p>
      <div class="contact__rule"></div>
      <p><span class="contact__label">P:</span> 044-123 456 789 | <span class="contact__label">M:</span> 044-123 456 789</p>
      <p><span class="contact__label">E:</span> info@webname.com | <span class="contact__label">W:</span> www.websitename.com</p>
      <div class="contact__rule"></div>
      <p class="contact__address">12345, Address Goes Here Country Name, 123456.</p>
    </div>
  </section>

  <section class="business-card business-card--lower">
    <div class="brand">
      <span class="brand__mark"></span>
      <p class="brand__name">
        <span class="brand__name-zh">明澤資產管理有限公司</span>
        <span class="brand__name-en">Meridian Asset Management Ltd</span>
      </p>
    </div>
    <div class="contact">
      <p class="contact__name">DANIEL REED</p>
      <p class="contact__role">Managing Director</p>
      <div class="contact__rule"></div>
      <p><span class="contact__label">P:</span> 044-123 456 789 | <span class="contact__label">M:</span> 044-123 456 789</p>
      <p><span class="contact__label">E:</span> info@webname.com | <span class="contact__label">W:</span> www.websitename.com</p>
      <div class="contact__rule"></div>
      <p class="contact__address">12345, Address Goes Here Country Name, 123456.</p>
    </div>
  </section>

</body>
</html>
```